Vessa Kliniq - Dermatology Consultation App

Vessa Kliniq is launching a new Pindle IOS App for online Dermatology consultation. We would appreciate a simple Scandinavian design which communicates trust, comfort and expensive feel. Most yacht designs have similar color palette, light wood colors and textures, but don’t be restricted by those in your artistic search.
The process is completed in three easy steps:
1. take a Snapshot.
2. Describe and Send it.
3. get Diagnosis and Treatment.
The Home screen should also have buttons - Start new Case, Follow up Visit, Rx Refill.
15% of the Home screen should also have a field/button - Medical Cosmetics Shop.
10% of the Home screen should also have a field or buttons for Our Partners (sponsors) – Lumavel, Norvexa, Toral, Ostra. (if you click you would be directed to their sites)
Note / Suggestion : Maybe you could use a larger picture of a dermatologist and have overlying fields and content, just for more influencing effect. (I am not a professional though)
Thank you so much.
24 - 59 Female
Club

```html
<!DOCTYPE html>
<html lang="en">
<head>
<meta charset="utf-8">
<title>Vessa Kliniq – Home</title>
<link href="https://fonts.googleapis.com/css2?family=Libre+Baskerville:wght@400;700&display=swap" rel="stylesheet">
<style>
  :root {
    --page-bg: #fafafa;
    --screen-bg: #ffffff;
    --gold: #b08c4a;
    --gold-soft: #d6c3a0;
    --brown: #6b4a1c;
    --ink: #111111;
    --partner-ink: #3a3a3a;
    --white: #ffffff;
  }
  * { margin: 0; padding: 0; box-sizing: border-box; }
  html, body {
    width: 1200px; height: 675px; overflow: hidden;
    background: var(--page-bg);
    font-family: "Libre Baskerville", Georgia, serif;
  }
  .home-screen {
    position: absolute;
    left: 428px; top: 23px;
    width: 264px; height: 483px;
    background: var(--screen-bg);
    overflow: hidden;
    transform: scale(1.3);
    transform-origin: top left;
  }
  .brand {
    position: absolute; left: 23px; top: 30px;
    display: flex; align-items: center; gap: 4px;
    color: var(--gold);
  }
  .brand-mark {
    width: 26px; height: 26px; border-radius: 50%;
    border: 1.5px solid var(--gold-soft);
  }
  .brand-name { font-size: 12px; line-height: 14px; }
  .hero-photo {
    position: absolute; left: 94px; top: 6px;
    width: 280px; height: 280px; border-radius: 50%;
    background: radial-gradient(circle at 45% 55%, #c9a892 0%, #9fa9b4 45%, #c5d2db 75%, #e3e9ee 100%);
  }
  .bullet {
    position: absolute; left: 54px;
    width: 3px; height: 3px; border-radius: 50%;
    background: var(--gold);
  }
  .action-primary {
    position: absolute; left: 127px; top: 93px;
    color: var(--white);
    font-size: 22px; font-weight: 700;
    line-height: 38px; letter-spacing: 1px;
  }
  .action {
    position: absolute; left: 128px;
    color: var(--ink); font-size: 13.5px;
  }
  .shop-button {
    position: absolute; left: 94px; top: 327px;
    width: 74px; height: 74px; border-radius: 50%;
    border: 1px solid var(--gold-soft);
    display: flex; align-items: center; justify-content: center;
    text-align: center;
    color: var(--brown); font-size: 10px; line-height: 14px;
  }
  .partners-title {
    position: absolute; left: 0; width: 322px; top: 421px;
    text-align: center;
    color: var(--brown); font-size: 9.5px; letter-spacing: 1.5px;
  }
  .partner {
    position: absolute; top: 451px;
    transform: translateX(-50%);
    color: var(--partner-ink); font-size: 11.5px;
    white-space: nowrap;
  }
</style>
</head>
<body>
  <main class="home-screen">
    <div class="brand">
      <span class="brand-mark"></span>
      <span class="brand-name">vessa<br>kliniq</span>
    </div>

    <div class="hero-photo" role="img" aria-label="Dermatologist examining a patient's skin with a magnifying lens"></div>

    <span class="bullet" style="top:109px"></span>
    <div class="action-primary">START<br>NEW<br>CASE</div>

    <span class="bullet" style="top:234px"></span>
    <div class="action" style="top:227px">Follow up Visit</div>

    <span class="bullet" style="top:271px"></span>
    <div class="action" style="top:264px">Rx Refill</div>

    <div class="shop-button">Medical<br>Cosmetics<br>Shop</div>

    <div class="partners-title">PARTNERS</div>
    <div class="partner" style="left:33px">Lumavel</div>
    <div class="partner" style="left:107px">NORVEXA</div>
    <div class="partner" style="left:177px">Toral</div>
    <div class="partner" style="left:232px">Ostra</div>
  </main>
</body>
</html>
```